Business Card Design Project

I am looking for a minimal matte background/shiny (spot UV) ink monochromatic design with a splash of neon color.

the card should be 2 sided, logo only on one side - all info and possibly logo on the other.

My creative director described the colors he imagined for the design to be:
'it's a dark field, like charcoal or a really dark burgundy, or deep blue, shot through with a neon—but just a tiny bit of it. so a charcoal field with a laser-thin streak of electric lime, safety orange, or cobalt blue. really beautiful stuff.'

here are some samples of the types of cards I am trying to create:
http://www.pictavault.example/photos/dawnpress/6967376935/in/photostream -> Vandrelle Lustre

http://www.pictavault.example/photos/dawnpress/6497659409/in/photostream -> Standard Coated (14pt/matte) with SPOT UV

http://www.pictavault.example/photos/dawnpress/6497658995/in/photostream/ -> Heavy Corvane with Raised Ink

http://www.pictavault.example/photos/dawnpress/6275629165/in/photostream/ -> Standard Coated (14pt/matte) with SPOT UV

Here is my logo:
https://www.filecrate.example/s/sigym192mlh58ge/quillorb%20logotype%20final.ai

Here are the details for info:
Dorian Elwood Marsh
email - dorian@quillorb.example
mobile - 555 013 2867
web -
quillorb.example: inventive technology applications
quillorb-tv.example: innovative video advertising

please let me know if there is anything at all that you need.

Target Market(s)

mid to large agencies that require interactive design and entrepreneurial/startup individuals/companies that need application development.

Industry/Entity Type

Safety

Requirements
Must have
• logo only on one side

```html
<!DOCTYPE html>
<html lang="en">
<head>
<meta charset="utf-8">
<title>Quillorb business card</title>
<link rel="stylesheet" href="https://fonts.googleapis.com/css2?family=Oswald:wght@400&family=Playfair+Display:wght@800&family=Questrial&display=swap">
<style>
  :root {
    --backdrop: #e4e9e9;
    --card: #111214;
    --band: #3a3c0e;
    --band-ink: #2d2f0a;
    --neon-yellow: #eef711;
    --neon-lime: #b4f01c;
    --detail-grey: #5d6166;
  }
  html, body {
    margin: 0;
    padding: 0;
    width: 1179px;
    height: 1200px;
    overflow: hidden;
    background: var(--backdrop);
  }
  .canvas {
    position: relative;
    width: 1179px;
    height: 1200px;
  }
  .card {
    position: absolute;
    left: 210px;
    width: 760px;
    height: 434px;
    background: var(--card);
    overflow: hidden;
  }
  .card--info { top: 110px; }
  .card--logo { top: 630px; }

  /* Info side */
  .brand-band {
    position: absolute;
    top: 0;
    right: 0;
    width: 146px;
    height: 100%;
    background: var(--band);
  }
  .brand-band__name {
    position: absolute;
    top: 50%;
    left: 50%;
    transform: translate(-50%, -50%) rotate(90deg);
    font-family: "Oswald", sans-serif;
    font-size: 60px;
    letter-spacing: 10px;
    color: var(--band-ink);
    white-space: nowrap;
  }
  .accent-bar {
    position: absolute;
    left: 62px;
    top: 236px;
    width: 66px;
    height: 172px;
    background: var(--neon-yellow);
  }
  .contact {
    position: absolute;
    left: 146px;
    top: 230px;
  }
  .contact__name {
    margin: 0 0 6px;
    font-family: "Playfair Display", serif;
    font-weight: 800;
    font-size: 24px;
    letter-spacing: 2px;
    color: var(--neon-yellow);
  }
  .contact__line {
    margin: 0;
    font-family: "Questrial", sans-serif;
    font-size: 13px;
    line-height: 19px;
    letter-spacing: 2.6px;
    color: var(--detail-grey);
  }
  .contact__label--web { color: var(--neon-yellow); }

  /* Logo side */
  .wordmark {
    position: absolute;
    left: 70px;
    top: 172px;
    display: flex;
    align-items: flex-start;
    gap: 18px;
  }
  .wordmark__name {
    font-family: "Oswald", sans-serif;
    font-size: 104px;
    line-height: 1;
    letter-spacing: 24px;
    color: var(--neon-lime);
  }
  .wordmark__square {
    width: 22px;
    height: 22px;
    margin-top: -30px;
    background: var(--neon-lime);
  }
</style>
</head>
<body>
<main class="canvas">
  <section class="card card--info" aria-label="Card back with contact details">
    <div class="brand-band"><span class="brand-band__name">QUILLORB</span></div>
    <div class="accent-bar"></div>
    <div class="contact">
      <h1 class="contact__name">Dorian Elwood Marsh</h1>
      <p class="contact__line">email - dorian@quillorb.example</p>
      <p class="contact__line">mobile - 555 013 2867</p>
      <p class="contact__line"><span class="contact__label--web">web -</span></p>
      <p class="contact__line">quillorb.example: inventive technology</p>
      <p class="contact__line">applications</p>
      <p class="contact__line">quillorb-tv.example: innovative video ad-</p>
      <p class="contact__line">vertising</p>
    </div>
  </section>

  <section class="card card--logo" aria-label="Card front with logo">
    <div class="wordmark">
      <span class="wordmark__name">QUILLORB</span>
      <span class="wordmark__square"></span>
    </div>
  </section>
</main>
</body>
</html>
```